Desing a brochure for Yachting Company

Our company brochure. We want something very special. We will use this brochure for our sister agencies and also for direct customer. So something should be good for both part.

- We need it in *cdr to possible editing ourselves.
- The size is 28.5 cm to 20 cm. Horizontal.
- Please find the attached file for a simple which we like it very much. Tonality, desing etc. looks good.
- Our company base colours #be9c4f and #1e2a38. Also you can make in our other two colours if do you feel it will look better #055ea2 and #86a42a
Details
- 1 page front cover page
- 1 page back cover page
- 1 page company profile
- 1 page introductory article
- 4 different new topic home page. ( like transition page)
- 1 Page desitination page (included some photos and destination highlights)
- 1 Page for a sample route ( intinerary) included map like attached sample.
- 1 yacht detail full page (some technical details and photos)
- 1 yacht detail page for 2 yachts. (2 yachts will be in same page. some technical details and photos)
- 1 yacht detail page for 3 yachts. (3 yachts will be in same page. some technical details and photos)
- 1 yacht detail page for 4 yachts. (4 yachts will be in same page. some technical details and photos)
- 1 yacht detail page for 6 yachts. (6 yachts will be in same page. some technical details and photos)

* you can use sample photos for yacht details.

Yacht details will be provide these information.
Yacht Name : Test
Guest Capacity : 10 person
Length : 35 meter
Category : Luxury
Price from : [url removed, login to view] Euro / per day
* these four items can be highlighted more, also can use some desing attraction in different part of page.

Total Cabin : 6
Double Cabin : 1
Single Cabin : 2
Triple Cabin : 2
Twin Cabin : 1
Crew : 3
Built & Refit Date :2008 / 2013

Please feel free to contact for any question or request.

Thank you

```html
<!DOCTYPE html>
<html lang="en">
<head>
<meta charset="utf-8">
<title>Example Yachting Co. – Brochure Spread</title>
<link href="https://fonts.googleapis.com/css2?family=EB+Garamond:wght@400;500&family=Open+Sans:wght@400;600&display=swap" rel="stylesheet">
<style>
  :root{
    --navy:#1e2a38;
    --navy-soft:#2f3f4f;
    --gold:#be9c4f;
    --paper:#ffffff;
    --backdrop:#8d847d;
    --ink-muted:#6b7480;
  }
  *{box-sizing:border-box;margin:0;padding:0}
  html,body{width:1200px;height:900px;overflow:hidden}
  body{background:var(--backdrop);display:flex;align-items:center;justify-content:center}
  .spread{display:flex;width:1120px;height:393px;box-shadow:0 12px 30px rgba(0,0,0,.25)}
  .page{position:relative;width:560px;height:393px;background:var(--paper);overflow:hidden}
  .page--left{border-right:1px solid #e3e3e3}

  .photo{position:absolute}
  .photo--sailing{left:0;top:0;width:262px;height:393px;
    background:linear-gradient(180deg,#e9edf1 0%,#dfe5eb 55%,#8aa0b6 75%,#3f5e7e 100%)}
  .photo--rope{left:272px;top:0;width:288px;height:190px;
    background:linear-gradient(160deg,#e2e6ea 0%,#c8cfd6 50%,#9aa5b0 100%)}
  .photo--deck{left:272px;top:198px;width:288px;height:195px;
    background:linear-gradient(200deg,#fbf3dc 0%,#cdd6dc 40%,#5f7890 75%,#2e4559 100%)}

  .nav{position:absolute;left:14px;right:14px;top:14px;height:16px;background:var(--navy);
    display:flex;align-items:center;font-family:"Open Sans",sans-serif;font-size:7px;color:#dfe3e8}
  .nav__item{padding:0 12px;height:100%;display:flex;align-items:center;white-space:nowrap}
  .nav__item--active{background:var(--gold);color:var(--navy);font-weight:600}
  .nav__brand{margin-left:auto;padding-right:10px;display:flex;align-items:center;gap:5px;
    font-family:"Open Sans",sans-serif;font-size:7px;color:var(--gold);white-space:nowrap}
  .nav__brand-mark{width:6px;height:6px;border-radius:50%;background:var(--gold)}

  .intro-band{position:absolute;left:0;right:0;top:68px;height:222px;
    background:linear-gradient(90deg,var(--navy) 0%,var(--navy-soft) 100%);
    display:flex;align-items:center;padding:0 24px}
  .intro-band__col{flex:1;font-family:"EB Garamond",serif;font-size:12.5px;line-height:1.35;color:var(--gold);padding:0 18px}
  .intro-band__divider{width:1px;height:150px;background:rgba(190,156,79,.55)}

  .footer{position:absolute;bottom:14px;font-family:"Open Sans",sans-serif;font-size:6.5px;color:var(--ink-muted);letter-spacing:.06em}
  .footer--left{left:18px;text-transform:uppercase}
  .footer--right{right:18px}
</style>
</head>
<body>
  <div class="spread">
    <section class="page page--left">
      <div class="photo photo--sailing" role="img" aria-label="Photo of a sailing yacht with white sails on the open sea"></div>
      <div class="photo photo--rope" role="img" aria-label="Photo of a coiled mooring rope on a yacht deck"></div>
      <div class="photo photo--deck" role="img" aria-label="Photo of a yacht deck cruising over the sea at sunset"></div>
    </section>

    <section class="page page--right">
      <nav class="nav">
        <span class="nav__item nav__item--active">Luxury Yacht Charter</span>
        <span class="nav__item">Luxury Yacht for Sale</span>
        <span class="nav__item">Example Yachting</span>
        <span class="nav__item">Tour Info</span>
        <span class="nav__item">Management</span>
        <span class="nav__brand"><span class="nav__brand-mark"></span>Example Yachting Co.</span>
      </nav>

      <div class="intro-band">
        <p class="intro-band__col">Visit our Luxury Yacht Charter section for a large selection of Gulets, Motor Yachts, Mega Yachts, Sailing Yachts and Bareboats. Looking for a yacht charter in Turkey, Greece or Croatia? You deserve the best personal attention so be assured we will find the ideal luxury yacht charter for you for any occasion.</p>
        <span class="intro-band__divider"></span>
        <p class="intro-band__col">Example Yachting Co. is Turkey's premier luxury yacht sales company and specialises in providing the finest luxury yachts. If you are looking to buy a luxury yacht or have luxury yachts for sale, pair up with us. Sale of some of the luxurious yachts ranging from 20 m to 100 m.</p>
      </div>

      <p class="footer footer--left">Luxury Yacht Charter &amp; For Sale</p>
      <p class="footer footer--right">www.example.com</p>
    </section>
  </div>
</body>
</html>
```